Brookvale Strategy Partners Website Design

I need a website design for my new business consulting and executive coaching firm, Brookvale Strategy Partners. We provide consultative services to business C-suites as well as personal coaching to executives. I have attached the logo with color scheme I have chosen. I would like the website to reflect professionalism and continue the color scheme in the logo.

Target Market(s)

Small to medium business and their executives; middle to upper income men and women in mid- to late career looking for significance

Industry/Entity Type

Business Consultant

Number of Pages Required

4 page

Requirements
Must have
• A homepage with prominent logo and way to contact for more information; an area on the homepage with easy to read, clear text to describe what the company does; a prominent area on the homepage for a tagline; a blog page that can be updated regularly, an "about us" page with biographical information; an "about us" page; a page detailing services offered
• The web design must match the logo colors and font that I have uploaded.
Nice to have
• A lighthouse picture in the background or header
Should not have
• A lot of text area on the homepage

```html
<!DOCTYPE html>
<html lang="en">
<head>
<meta charset="utf-8">
<title>Brookvale Strategy Partners — Home</title>
<link rel="stylesheet" href="https://fonts.googleapis.com/css2?family=Gelasio:wght@400&family=Ubuntu:wght@300;400&display=swap">
<style>
  :root {
    --sky-top: #586d9b;
    --sky-mid: #c3ccd4;
    --sky-low: #d4a996;
    --page: #f8f8f8;
    --brand-red: #983a3e;
    --brand-navy: #2d3b6c;
    --text-soft: #c2c2c2;
    --text-mid: #a9a9a9;
    --rule: #dedede;
    --panel: #e9e9e9;
    --panel-edge: #d6d6d6;
    --hero-top: #a9bccb;
    --hero-glow: #d99a98;
    --hero-sea: #5e77a7;
    --hero-deep: #3f4f78;
  }
  * { box-sizing: border-box; margin: 0; padding: 0; }
  html, body { width: 979px; height: 1200px; overflow: hidden; }
  body {
    background: linear-gradient(180deg, var(--sky-top) 0%, var(--sky-mid) 45%, var(--sky-low) 100%);
    font-family: "Ubuntu", sans-serif;
    position: relative;
  }
  .page {
    position: absolute; left: 67px; top: 0; width: 842px; height: 1200px;
    background: var(--page);
  }
  .brand {
    position: absolute; left: 0; right: 0; top: 70px;
    display: flex; justify-content: center; align-items: center; gap: 10px;
    font-family: "Gelasio", serif; font-size: 22px; color: var(--brand-navy);
    letter-spacing: 0.5px;
  }
  .brand-mark { width: 14px; height: 14px; background: var(--brand-red); }
  .main-nav {
    position: absolute; left: 31px; top: 0; width: 782px; height: 177px;
    border-bottom: 1px solid var(--rule);
  }
  .main-nav a {
    position: absolute; top: 134px; font-family: "Gelasio", serif; font-size: 19px;
    color: var(--text-soft); text-decoration: none; letter-spacing: -0.3px;
  }
  .main-nav a.current { color: var(--brand-navy); }
  .main-nav .current-bar {
    position: absolute; left: 225px; top: 170px; width: 83px; height: 6px; background: var(--brand-red);
  }
  .tagline {
    position: absolute; left: 50px; top: 186px;
    font-family: "Ubuntu", sans-serif; font-style: italic; font-size: 27px;
    color: #dcdcdc; letter-spacing: -1.2px;
  }
  .tagline span { color: #ececec; margin-left: 10px; }
  .hero {
    position: absolute; left: 31px; top: 231px; width: 782px; height: 400px;
    background: linear-gradient(180deg, var(--hero-top) 0%, #c8b0b8 22%, var(--hero-glow) 52%, var(--hero-sea) 60%, var(--hero-sea) 82%, var(--hero-deep) 100%);
  }
  .section-head {
    position: absolute; top: 648px; height: 48px;
    font-family: "Gelasio", serif; font-size: 27px; color: var(--text-soft); letter-spacing: -1.5px;
  }
  .section-head svg { position: absolute; right: 0; top: 10px; }
  .heads-rule { position: absolute; left: 31px; top: 694px; width: 782px; border-top: 2px solid var(--rule); }
  .news {
    position: absolute; left: 31px; top: 706px; width: 272px; height: 257px;
    background: var(--panel); border: 2px solid var(--panel-edge); padding: 14px 14px 0 14px;
  }
  .news-item { border-bottom: 2px solid #d8d8d8; padding: 4px 0 10px 2px; margin-bottom: 12px; }
  .news-date { font-size: 10px; color: var(--text-mid); letter-spacing: -0.4px; }
  .news-title { font-size: 15px; color: var(--text-soft); letter-spacing: -0.7px; margin-top: 8px; line-height: 20px; }
  .news-item.active .news-title { color: var(--brand-red); }
  .news-item.active { border-bottom-color: var(--brand-red); border-bottom-width: 1px; }
  .info {
    position: absolute; left: 323px; top: 704px; width: 490px;
    font-family: "Gelasio", serif; font-size: 23px; line-height: 27px;
    color: var(--text-soft); letter-spacing: -0.6px;
  }
  .info p + p { margin-top: 26px; }
  .info .hl-red { color: var(--brand-red); }
  .info .hl-navy { color: var(--brand-navy); }
  .btn {
    background: var(--brand-red); color: #fff; border: none;
    font-family: "Gelasio", serif; font-size: 18px;
  }
  .btn-continue { position: absolute; left: 701px; top: 919px; width: 87px; height: 31px; }
  .footer {
    position: absolute; left: 31px; top: 977px; width: 781px; height: 223px;
    border: 1px solid #e6e6e6; border-bottom: none;
  }
  .footer-col { position: absolute; top: 16px; height: 154px; }
  .footer-col + .footer-col { border-left: 1px solid #e6e6e6; }
  .footer h3 { font-weight: 400; font-size: 20px; color: var(--text-soft); letter-spacing: -0.8px; }
  .contact { left: 0; width: 282px; padding: 31px 0 0 32px; }
  .contact svg { position: absolute; right: 24px; top: 34px; }
  .contact ol { list-style: none; margin-top: 20px; color: var(--text-mid); font-size: 15px; letter-spacing: -0.6px; }
  .contact li { margin-bottom: 16px; }
  .contact li b { font-weight: 400; margin-right: 10px; }
  .links { left: 282px; width: 201px; padding: 31px 0 0 27px; }
  .links svg { position: absolute; right: 37px; top: 36px; }
  .links nav { display: grid; grid-template-columns: 78px 60px; row-gap: 24px; margin-top: 22px; }
  .links nav a { font-size: 12px; color: var(--text-mid); text-decoration: none; letter-spacing: -0.4px; }
  .search { left: 483px; width: 298px; }
  .search-field { position: absolute; left: 14px; top: 12px; width: 189px; height: 30px; border: 1px solid #e4e4e4; background: #fbfbfb; }
  .btn-search { position: absolute; left: 203px; top: 12px; width: 70px; height: 30px; font-size: 17px; }
  .social { position: absolute; top: 79px; left: 73px; display: flex; gap: 26px; }
  .social span { display: block; width: 32px; height: 32px; background: #d5d5d5; border-radius: 3px; }
  .footer-bar {
    position: absolute; left: 31px; top: 168px; width: 729px; height: 38px;
    border: 1px solid #e6e6e6; padding: 11px 14px; font-size: 12px; color: var(--text-mid);
  }
</style>
</head>
<body>
  <div class="page">
    <header>
      <div class="brand"><span class="brand-mark"></span>Brookvale Strategy Partners</div>
      <nav class="main-nav">
        <a class="current" href="#" style="left:197px">Home</a>
        <a href="#" style="left:333px">Services</a>
        <a href="#" style="left:465px">About Us</a>
        <a href="#" style="left:596px">Blog</a>
        <span class="current-bar"></span>
      </nav>
      <p class="tagline">Your tagline goes here,<span>and extends up until here.</span></p>
    </header>

    <div class="hero" role="img" aria-label="Lighthouse on a rocky shore at dusk, beam across a pink sky over calm blue sea"></div>

    <h2 class="section-head" style="left:31px;width:262px">Some News Here
      <svg width="20" height="20" viewBox="0 0 20 20" fill="none" stroke="#c8c8c8" stroke-width="1.5"><rect x="1" y="1" width="18" height="18"/><line x1="4" y1="5" x2="16" y2="5"/><line x1="10" y1="9" x2="16" y2="9"/><line x1="10" y1="12" x2="16" y2="12"/><line x1="4" y1="15" x2="16" y2="15"/><rect x="4" y="8" width="4" height="5"/></svg>
    </h2>
    <h2 class="section-head" style="left:323px;width:490px">Some information here
      <svg width="22" height="20" viewBox="0 0 22 20" fill="none" stroke="#c8c8c8" stroke-width="1.5"><rect x="1" y="1" width="20" height="4"/><rect x="1" y="8" width="20" height="4"/><rect x="5" y="15" width="12" height="4"/></svg>
    </h2>
    <div class="heads-rule"></div>

    <aside class="news">
      <article class="news-item"><p class="news-date">Jan 1, 2016 Friday</p><p class="news-title">Ac convallis sem lacus vitae ex.</p></article>
      <article class="news-item active"><p class="news-date">Jan 1, 2016 Friday</p><p class="news-title">Ac convallis sem lacus vitae ex.</p></article>
      <article class="news-item"><p class="news-date">Jan 1, 2016 Friday</p><p class="news-title">Ac convallis sem lacus vitae ex. Proin lacinia sed.</p></article>
    </aside>

    <section class="info">
      <p>Lorem ipsum dolor sit amet, consectetur adipiscing elit. Integer egestas elit lectus, et <span class="hl-red">is Brookvale test</span> lorem ornare quis.</p>
      <p>Fusce commodo, <span class="hl-navy">strategy partners test</span> lobortis posuere, tortor eros efficitur purus, ac convallis sem lacus vitae ex. Proin lacinia sed sem vitae ultricies.</p>
    </section>
    <button class="btn btn-continue">Continue</button>

    <footer class="footer">
      <div class="footer-col contact">
        <h3>Contact here</h3>
        <svg width="26" height="20" viewBox="0 0 26 20" fill="none" stroke="#999" stroke-width="1.5"><rect x="1" y="1" width="24" height="18"/><circle cx="8" cy="8" r="2.5" fill="#999"/><path d="M4 15c1-3 7-3 8 0" fill="#999"/><line x1="14" y1="7" x2="21" y2="7"/><line x1="14" y1="11" x2="21" y2="11"/><line x1="14" y1="15" x2="21" y2="15"/></svg>
        <ol><li><b>1:</b>xxx - xxx - xxxxx</li><li><b>2:</b>xxx - xxx - xxxxx</li></ol>
      </div>
      <div class="footer-col links">
        <h3>Links</h3>
        <svg width="18" height="18" viewBox="0 0 18 18" fill="none" stroke="#999" stroke-width="2"><path d="M8 10l-3 3a2.5 2.5 0 0 1-3.5-3.5l3-3"/><path d="M10 8l3-3a2.5 2.5 0 0 0-3.5-3.5l-3 3"/><line x1="6.5" y1="11.5" x2="11.5" y2="6.5"/></svg>
        <nav><a href="#">Home</a><a href="#">About Us</a><a href="#">Services</a><a href="#">Blog</a></nav>
      </div>
      <div class="footer-col search">
        <input class="search-field" type="text" aria-label="Search">
        <button class="btn btn-search">Search</button>
        <div class="social"><span aria-label="Social link"></span><span aria-label="Social link"></span><span aria-label="Social link"></span></div>
      </div>
      <div class="footer-bar">12/29/2015</div>
    </footer>
  </div>
</body>
</html>
```